Packaging for Hair Fibers Product

We are a start up company looking for a new packaging design for hair building fibers. These are aimed at predominantly men but also women as well. We already have a logo and i have the packaging design from our competitors. We are wanting to keep the look masculine as 90% of our users will be middle aged men. We would like the colours to be black and white but are open to other colours as well.
It will need to have our logo and the following somewhere on the front.
"Instant Fuller & Thicker Hair" & "Natural Hair Building Fibers" "28g" or "Net Weight 28g"
We only need the front of the packaging designed, please make the other sides of the packaging the same colour but blank.
Target Market(s)
Men 25+
Industry/Entity Type
Hair And Beauty
Requirements
Must have
- Logo which i have included. and the following somewhere on the front.
- "Instant Fuller & Thicker Hair" ; "Natural Hair Building Fibers" "28g" or "Net Weight 28g"
Nice to have
- Make it stand out from the competition or similar to the brantiq example.

```html
<!DOCTYPE html>
<html lang="en">
<head>
<meta charset="utf-8">
<title>Tressline Hair Building Fibers – Front Label</title>
<link href="https://fonts.googleapis.com/css2?family=Oswald:wght@300;400&family=Roboto+Condensed:wght@400;700&display=swap" rel="stylesheet">
<style>
  :root {
    --backdrop: #1b1a18;
    --pack-black: #0d0d0d;
    --cap-black: #070707;
    --cap-sheen: #1f1f1f;
    --ink-white: #f2f0ea;
    --band-white: #f4f3ef;
    --band-ink: #111111;
  }
  * { margin: 0; padding: 0; box-sizing: border-box; }
  html, body {
    width: 1200px;
    height: 1000px;
    overflow: hidden;
    background: var(--backdrop);
  }
  .canvas {
    position: relative;
    width: 1200px;
    height: 1000px;
    background: var(--backdrop);
  }
  .pack-front {
    position: absolute;
    left: 410px;
    top: 110px;
    width: 380px;
    height: 790px;
    background: var(--pack-black);
    border-radius: 8px;
    overflow: hidden;
  }
  .pack-cap {
    position: absolute;
    left: 0; top: 0;
    width: 100%;
    height: 118px;
    background: linear-gradient(90deg, var(--cap-black) 0%, var(--cap-sheen) 48%, var(--cap-black) 100%);
    border-bottom: 2px solid #000;
  }
  .brand {
    position: absolute;
    top: 395px;
    left: 0;
    width: 100%;
    display: flex;
    align-items: center;
    justify-content: center;
    gap: 14px;
  }
  .brand-mark {
    width: 12px;
    height: 12px;
    background: var(--ink-white);
  }
  .brand-name {
    font-family: 'Roboto Condensed', sans-serif;
    font-weight: 400;
    font-size: 25px;
    letter-spacing: 7px;
    color: var(--ink-white);
    text-transform: uppercase;
  }
  .headline {
    position: absolute;
    top: 520px;
    left: 26px;
    width: 330px;
    height: 130px;
    font-family: 'Oswald', sans-serif;
    color: var(--ink-white);
  }
  .headline-line {
    display: block;
    font-weight: 400;
    font-size: 49px;
    line-height: 52px;
    letter-spacing: -1px;
    text-transform: uppercase;
    transform: scaleX(0.82);
    transform-origin: left;
  }
  .headline-amp {
    position: absolute;
    right: -6px;
    top: 8px;
    font-weight: 300;
    font-size: 112px;
    line-height: 1;
  }
  .descriptor-band {
    position: absolute;
    top: 670px;
    left: 14px;
    right: 14px;
    height: 40px;
    background: var(--band-white);
    display: flex;
    align-items: center;
    justify-content: center;
  }
  .descriptor {
    font-family: 'Roboto Condensed', sans-serif;
    font-weight: 700;
    font-size: 21px;
    color: var(--band-ink);
    text-transform: uppercase;
    letter-spacing: 0.3px;
  }
  .net-weight {
    position: absolute;
    top: 738px;
    left: 0;
    width: 100%;
    text-align: center;
    font-family: 'Roboto Condensed', sans-serif;
    font-weight: 700;
    font-size: 27px;
    color: var(--ink-white);
    letter-spacing: 1px;
  }
</style>
</head>
<body>
  <main class="canvas">
    <section class="pack-front">
      <div class="pack-cap"></div>

      <div class="brand">
        <span class="brand-mark"></span>
        <span class="brand-name">Tressline</span>
      </div>

      <h1 class="headline">
        <span class="headline-line">Instant Fuller</span>
        <span class="headline-line">Thicker Hair</span>
        <span class="headline-amp">&amp;</span>
      </h1>

      <div class="descriptor-band">
        <p class="descriptor">Natural Hair Building Fibers</p>
      </div>

      <p class="net-weight">28G</p>
    </section>
  </main>
</body>
</html>
```